Business Card Design Project

Design a business card for a new entity that is in the OTC (over-the-counter-derivative brokering business-Financial Services.
The card should be clean a professional looking. We encourage designers to think pro-actively, fresh and innovative, but also keep in mind that only 2 things are important. a)that the card look professional b)that it is somehow memorable.

We have a new logo which we will upload and will want the Trident symbol in the logo to be raised OR not have the symbol raised and plan on having the word " BROKERAGE SERVICES" raised that stands out and will look sharp.

Along with uploading the new logo which MUST be incorperated, I am also going to upload 3 different business cards of other businesses to use only as guild-lines since I think they are clean and professional looking BUT I encourage all to be pro-active and creative on their own.

Industry/Entity Type

Business

Requirements
Must have
• 1. MUST HAVE THE NEW LOGO WHICH WILL BE UPLOADED
2. MUST HAVE A VERSION SIMILAR TO THE 3 DIFFERENT BUSINESS CARDS I WILL UPLOAD, BUT EACH DESIGNER MUST ONLY THESE THIS FORMAT AS A BACK-UP AND BE CREATIVE ON THEIR OWN FIRST. ALSO WHEN LOOKING AT THE CARDS WHICH I UPLOAD TO USE AS A GUILD-LINE KEEP IN MIND THAT THESE ARE PINNACLE 300 COMPANIES SO DO NOT MIMIC ONLY USE FOR IDEAS.
Nice to have
• these are the 3 different other biz cards to look at for some reference

```html
<!DOCTYPE html>
<html lang="en">
<head>
<meta charset="utf-8">
<title>Meridian Brokerage Services – Business Cards</title>
<link rel="stylesheet" href="https://fonts.googleapis.com/css2?family=Source+Sans+3:wght@400;600&display=swap">
<style>
  :root {
    --backdrop: #5a5a5c;
    --card-black: #0b0b0b;
    --panel-white: #eef0ef;
    --gold-light: #f2bd1f;
    --gold-deep: #c8901f;
    --ink-grey: #3a3a3a;
    --ink-mid: #555555;
    --text-light: #f4f4f4;
  }
  html, body {
    margin: 0;
    padding: 0;
    width: 1200px;
    height: 900px;
    overflow: hidden;
    background: var(--backdrop);
    font-family: "Source Sans 3", "Myriad Pro", Arial, sans-serif;
  }
  .stage {
    position: relative;
    width: 1200px;
    height: 900px;
  }
  .card {
    position: absolute;
    top: 150px;
    width: 360px;
    height: 600px;
    box-shadow: 0 14px 30px rgba(0,0,0,0.45);
  }
  .card--contact { left: 210px; }
  .card--brand   { left: 630px; }
  .card svg { display: block; }

  .frame-black  { fill: var(--card-black); }
  .panel-white  { fill: var(--panel-white); }

  .brand-name {
    font-family: "Source Sans 3", Arial, sans-serif;
    font-weight: 600;
    fill: var(--ink-grey);
  }
  .brand-name--small { font-size: 17px; letter-spacing: 1px; }
  .brand-name--large { font-size: 30px; letter-spacing: 1.5px; }
  .brand-mark { fill: var(--ink-grey); }

  .person-name { font-size: 27px; font-weight: 400; fill: var(--ink-mid); }
  .person-role { font-size: 17px; font-weight: 400; fill: var(--ink-mid); }

  .contact-line { font-size: 16px; font-weight: 400; fill: var(--text-light); }
  .contact-icon-box { fill: none; stroke: var(--text-light); stroke-width: 1.6; }
  .contact-icon-glyph { fill: var(--text-light); }

  .website { font-size: 17px; font-weight: 400; fill: var(--gold-light); letter-spacing: 0.3px; }
</style>
</head>
<body>
<main class="stage">

  <!-- Contact side -->
  <section class="card card--contact" aria-label="Business card, contact side">
    <svg width="360" height="600" viewBox="0 0 360 600">
      <defs>
        <linearGradient id="goldFill" x1="0" y1="0" x2="1" y2="1">
          <stop offset="0" stop-color="var(--gold-light)"/>
          <stop offset="1" stop-color="var(--gold-deep)"/>
        </linearGradient>
      </defs>
      <rect class="frame-black" width="360" height="600"/>

      <!-- brand line -->
      <rect class="brand-mark" x="108" y="24" width="22" height="22"/>
      <text class="brand-name brand-name--small" x="140" y="33">MERIDIAN</text>
      <text class="brand-name brand-name--small" x="140" y="52" style="font-size:12px">BROKERAGE SERVICES</text>

      <!-- gold frame -->
      <polygon fill="url(#goldFill)" points="20,180 68,92 346,92 346,520 70,520 20,440"/>
      <!-- white name panel -->
      <polygon class="panel-white" points="80,195 112,106 332,106 332,355 80,280"/>

      <text class="person-name" x="150" y="200">Your Name</text>
      <text class="person-role" x="150" y="224">Job title</text>

      <!-- contacts -->
      <g class="contact-list">
        <rect class="contact-icon-box" x="70" y="352" width="16" height="16"/>
        <circle class="contact-icon-glyph" cx="78" cy="358" r="3"/>
        <polygon class="contact-icon-glyph" points="75,360 81,360 78,365"/>
        <text class="contact-line" x="96" y="365">Your Address goes here</text>

        <rect class="contact-icon-box" x="70" y="378" width="16" height="16"/>
        <rect class="contact-icon-glyph" x="75" y="381" width="6" height="10" rx="1.5"/>
        <text class="contact-line" x="96" y="391">000-000-0000</text>

        <rect class="contact-icon-box" x="70" y="404" width="16" height="16"/>
        <rect class="contact-icon-glyph" x="74" y="408" width="8" height="8"/>
        <text class="contact-line" x="96" y="417">000-000-0000</text>

        <rect class="contact-icon-box" x="70" y="430" width="16" height="16"/>
        <rect class="contact-icon-glyph" x="73" y="434" width="10" height="7"/>
        <text class="contact-line" x="96" y="443">name@domainname.com</text>
      </g>

      <text class="website" x="180" y="568" text-anchor="middle">www.websitename.com</text>
    </svg>
  </section>

  <!-- Brand side -->
  <section class="card card--brand" aria-label="Business card, brand side">
    <svg width="360" height="600" viewBox="0 0 360 600">
      <defs>
        <linearGradient id="goldFillFront" x1="0" y1="0" x2="1" y2="1">
          <stop offset="0" stop-color="var(--gold-light)"/>
          <stop offset="1" stop-color="var(--gold-deep)"/>
        </linearGradient>
      </defs>
      <rect class="frame-black" width="360" height="600"/>

      <!-- gold frame -->
      <polygon fill="url(#goldFillFront)" points="16,150 66,50 346,50 346,450 300,545 16,545"/>
      <!-- white panel -->
      <polygon class="panel-white" points="40,150 82,64 332,64 332,440 292,528 40,528"/>

      <!-- brand lockup -->
      <rect class="brand-mark" x="58" y="258" width="34" height="34"/>
      <text class="brand-name brand-name--large" x="104" y="285">MERIDIAN</text>
      <text class="brand-name brand-name--large" x="104" y="318" style="font-size:18px;letter-spacing:2px">BROKERAGE SERVICES</text>

      <text class="website" x="180" y="575" text-anchor="middle">www.websitename.com</text>
    </svg>
  </section>

</main>
</body>
</html>
```